Flyer Design for International Business Consultant

We need an advertisement to help build the profile of Miles Haversham, Senior Consultant and Director at 'ORB Advisory Group'.

What we want to promote:
Our Senior Consultant and Director, Miles Haversham as expert on all matters China related.

Who are we promoting to:
Industry associations and networking groups.

Why:
Many organisations are interested in reaching the Chinese market, however don't know who to go to or who to trust. With many consultants out there trying to claim they offer a similar service, ORB would like to promote Miles as a genuine expert in the field and the 'go to' person on all things China business related. To do this, we are in the process of building Miles's national and international profile, which includes advertising Miles expertise to industry associations and networking groups so that they consider booking Miles as a key note speaker at conferences. We know that our target audience are more inclined to seek the advice of someone they have seen speak at a conference than to find someone in the Golden listings or via findly search.

A Bit about Miles Haversham:

Miles Haversham has lived, worked and studied in China for extended periods, speaks and writes fluently in Chinese, was formerly a Member of the Tasmanian Government Trade Outreach Advisory Panel, is a member of the Institute of Global Commerce Studies and is a member of the Pacific Asia Enterprise Forum to name a few. To add to his credentials, Miles has by invitation lectured for 5 consecutive years in Management and Economics at Masters Level to students at Kowloon Harbour College.

Miles’s qualifications include: Bachelor of Arts (Asian Studies), Bachelor of Business (Applied Economics – International Trade), Master of Business in Applied Economics (International Business) and currently completing a Doctor of Business Administration (International Business Management) which has an economics focus and researches the export of Australian professional services to China.

Miles has been the Principal Consultant for a number of ORB’s clients including the recent assignment commissioned by Victorian based company BRN Freightways, who have benefited from a $40 million deal with Eastern Plains Locomotive (EPL). This project has also resulted in EPL, China’s largest train manufacturer decision to set up offices in Victoria.

Miles is an expert in Australia/China Business relations and has been paramount to the success of numerous international business transactions. As mentioned, Miles is not only fluent in spoken and written Mandarin, but is also a bi-cultural expert (meaning he knows both Australian and Chinese) cultures. From Australian and Chinese history, art, food and more, Miles Haversham provides his clients with more than translation services.

A Bit about ORB Advisory Group:

Run by experienced business executives with over 20 years’ experience in the Chinese and Australian markets, ORB brings a un-paralleled level of knowledge and expertise that enables cooperative business relations to develop between international organisations despite the language and cultural differences. They are a bi-lingual and bi-cultural international business consultancy that specialise in managing cross-border business involving China.

ORB has expertise in all facets of business management and has worked with a range of companies and organisations to develop and implement strategic business solutions to set direction, improve performance and maximise returns to stakeholders. ORB has particular expertise in economic and market analysis and specialises in project management of large and complex projects, strategic procurement, market research and market development strategies. Combined with their cultural and language skills, ORB provides a unique and high value contribution to international projects.

Good afternoon designers

Thank you for your submissions so far.  We are happy with some of the designs that have come in, however, many of you have produced flyers that have too much information in it.  We are looking for something more concise that does not appear to be either a copy of information I have posted in this brief or a fancy looking resume for Miles Haversham. 

Please remember, we are communicating to event co-ordinators who are looking to appoint guest speakers at an upcoming conference.  They want someone who is going to discuss some of the 'hot topics' their audience are interested in, someone who is experienced in the topic and someone who is interesting. We need to communicate all of this in a concise, and creative way so that we can make Miles Haversham stand out above the rest.

Dear Designers

Thank you all very much for your submissions.  We appreciate you taking the time to compose a flyer for our organisation. 

Regards
Rosa

Dear Designers

Regards
Rosa

Target Market(s)

Event/conference managers or coordinators

Industry/Entity Type

Business Management

Requirements
Must have
• Must have the ORB Logo on it (red, white and black). The ad will be in the form of an electronic flyer to be embedded in an email that will be sent on to relevant contacts in our database.

```html
<!DOCTYPE html>
<html lang="en">
<head>
<meta charset="utf-8">
<title>ORB Advisory Group – Miles Haversham</title>
<link rel="stylesheet" href="https://fonts.googleapis.com/css2?family=Roboto+Condensed:wght@700&family=Source+Sans+3:ital,wght@0,400;0,600;0,700;1,400&display=swap">
<style>
  :root {
    --page-bg: #f1f1f1;
    --card-bg: #ffffff;
    --frame: #8a8a8a;
    --brand-red: #e8121a;
    --ink: #1c1c1c;
    --ink-soft: #222222;
    --figure-dark: #3c3c3c;
    --figure-mid: #9a9a9a;
    --figure-light: #f4f4f4;
  }
  * { margin: 0; padding: 0; box-sizing: border-box; }
  html, body {
    width: 1200px; height: 852px; overflow: hidden;
    background: var(--page-bg);
  }
  .flyer {
    position: absolute; left: 60px; top: 45px;
    width: 1073px; height: 750px;
    background: var(--card-bg);
  }
  .flyer-frame {
    position: absolute; left: 36px; top: 43px;
    width: 993px; height: 619px;
    border: 1px solid var(--frame);
  }
  .people-visual {
    position: absolute; left: 560px; top: 44px;
    width: 468px; height: 617px;
    background: linear-gradient(180deg, var(--figure-dark) 0%, var(--figure-mid) 55%, var(--figure-light) 100%);
    opacity: .55;
    -webkit-mask-image: linear-gradient(90deg, transparent 0%, #000 22%);
            mask-image: linear-gradient(90deg, transparent 0%, #000 22%);
  }
  .brand {
    position: absolute; left: 63px; top: 62px;
    display: flex; align-items: center; gap: 22px;
  }
  .brand-mark {
    width: 158px; height: 158px;
    background: var(--brand-red);
  }
  .brand-name {
    font-family: "Roboto Condensed", sans-serif;
    font-weight: 700; color: var(--ink);
    line-height: 1;
  }
  .brand-name .brand-short { display: block; font-size: 104px; letter-spacing: 1px; }
  .brand-name .brand-long { display: block; font-size: 37px; margin-top: 4px; letter-spacing: .5px; }
  .consultant {
    position: absolute; left: 63px; top: 248px;
    font-family: "Source Sans 3", sans-serif;
  }
  .consultant-name {
    font-size: 62px; font-weight: 700; color: var(--brand-red);
    line-height: 1; letter-spacing: -.5px;
  }
  .consultant-role {
    font-size: 29px; font-style: italic; color: var(--ink);
    margin-top: 8px;
  }
  .expertise {
    position: absolute; left: 63px; top: 370px; width: 760px;
    font-family: "Source Sans 3", sans-serif; color: var(--ink-soft);
  }
  .expertise-heading {
    font-size: 27px; font-weight: 700; color: var(--brand-red);
    margin-bottom: 6px;
  }
  .expertise-list { list-style: none; font-size: 20.5px; line-height: 27.5px; }
  .expertise-list li { padding-left: 15px; text-indent: -15px; }
  .expertise-list li::before { content: "•"; display: inline-block; width: 15px; text-indent: 0; }
  .qualifications {
    position: absolute; left: 63px; top: 546px; width: 940px;
    font-family: "Source Sans 3", sans-serif;
    font-size: 16.5px; line-height: 23.5px; color: var(--ink-soft);
  }
  .qualifications-label { font-weight: 700; color: var(--brand-red); }
</style>
</head>
<body>
  <main class="flyer">
    <div class="people-visual" role="img" aria-label="Group of business people in suits walking forward, shown as grey silhouettes with soft reflections"></div>
    <div class="flyer-frame"></div>

    <header class="brand">
      <div class="brand-mark"></div>
      <div class="brand-name">
        <span class="brand-short">ORB</span>
        <span class="brand-long">ADVISORY GROUP</span>
      </div>
    </header>

    <section class="consultant">
      <h1 class="consultant-name">Miles Haversham</h1>
      <p class="consultant-role">Senior Consultant and Director</p>
    </section>

    <section class="expertise">
      <h2 class="expertise-heading">Expert on all matters China related</h2>
      <ul class="expertise-list">
        <li>&nbsp;Writes and speak fluently in Chinese</li>
        <li>Expert in Australia/China Business relations</li>
        <li>Bi-cultural expert&nbsp; from Australian and Chinese history, art, food and more,<br>Miles Haversham provides his clients with more than translation services.</li>
      </ul>
    </section>

    <p class="qualifications">
      <span class="qualifications-label">Qualifications:</span> Bachelor of Arts (Asian Studies), Bachelor of Business (Applied Economics – International Trade), Master of Business in Applied Economics (International Business) and currently completing a Doctor of Business Administration (International Business Management) which has an economics focus and researches the export of Australian professional services to China.
    </p>
  </main>
</body>
</html>
```